Door Hangers Advertisement for Real Estate Agent

Hi,

I need a set of 3 door hangers to advertise my real estate services. The design needs to be eye catching with the end goal of having ,y target audience contact me.

I have provided reference material and criteria to guide you. I am open to changes in language if you have something better in mind. My primary goal is to have them contact me.

I have attached a rough draft of what I have in mind. Compared to this design I would like the final product to stand out more and easier to read. Note the back will provide the bulk of the information regarding my services. The front needs to be the eye catching part.

Please let me know if you have any questions.

Target Market(s)

Individuals looking to sell or buy a house.

Industry/Entity Type

Real Estate Agent

Colors

Designer to choose colors to be used in the design.

Requirements
Must have
• See criteria document.

```html
<!DOCTYPE html>
<html lang="en">
<head>
<meta charset="utf-8">
<title>Harlow Estates – Door Hanger</title>
<link href="https://fonts.googleapis.com/css2?family=Montserrat:wght@700;800&family=Questrial&display=swap" rel="stylesheet">
<style>
  :root {
    --red: #e8323a;
    --dark: #2b2b2d;
    --sky-top: #3f97ee;
    --sky-bottom: #8ec8fb;
    --white: #ffffff;
    --ink: #1d1d1d;
  }
  * { box-sizing: border-box; margin: 0; padding: 0; }
  html, body { width: 960px; height: 1200px; overflow: hidden; background: var(--white); }
  body { position: relative; font-family: "Questrial", sans-serif; }

  .crop-marks { position: absolute; inset: 0; }

  .hanger { position: absolute; top: 160px; width: 386px; height: 912px; overflow: hidden; }
  .hanger--front { left: 70px; background: var(--white); }
  .hanger--back { left: 501px; background: var(--white); }

  .abs, .placeholder { position: absolute; }

  /* front */
  .front-sky { left: 0; top: 0; width: 386px; height: 480px;
    background: linear-gradient(180deg, var(--sky-top) 0%, #5aaaf4 40%, var(--sky-bottom) 100%); }
  .front-house { left: 0; top: 290px; width: 386px; height: 190px;
    background: linear-gradient(180deg, #4b6a4a 0%, #6b7a80 45%, #8c8f92 75%, #b9b8ae 100%); }
  .cardinal { background: var(--red); border-radius: 40% 55% 45% 50%; }
  .front-cardinal { left: 34px; top: 156px; width: 50px; height: 36px; }

  .tagline { left: 0; width: 386px; text-align: center; color: var(--white);
    font-size: 17.6px; line-height: 22px; letter-spacing: 0.2px; text-transform: uppercase; }
  .tagline--one { top: 195px; }
  .tagline--two { top: 243px; }
  .tag-mark { background: var(--red); padding: 0 3px; border-radius: 2px; }

  .front-dark { left: 0; top: 0; width: 386px; height: 912px; }

  .pitch { left: 32px; width: 345px; color: var(--white); }
  .pitch-title { font-family: "Montserrat", sans-serif; font-weight: 800; color: var(--red);
    font-size: 29px; line-height: 32px; letter-spacing: 0.5px; }
  .pitch-text { font-size: 18.5px; line-height: 20px; }
  .pitch--sell { top: 488px; }
  .pitch--buy { top: 566px; }

  .values { left: 126px; top: 678px; font-family: "Montserrat", sans-serif; font-weight: 800;
    font-size: 13.6px; line-height: 18.5px; text-transform: uppercase; color: var(--red); white-space: nowrap; }
  .values .plain { color: var(--white); }

  .name-band { left: 0; top: 748px; width: 386px; height: 64px; background: var(--red); }
  .front-name { right: 28px; top: 756px; color: var(--white); font-size: 25px; line-height: 26px; text-align: right; }
  .front-phone { right: 28px; top: 782px; color: var(--white); font-family: "Montserrat", sans-serif;
    font-weight: 700; font-size: 22.5px; line-height: 26px; text-align: right; }
  .front-email { right: 22px; top: 820px; font-size: 15.5px; color: var(--ink); text-align: right; }
  .brand { color: var(--red); font-family: "Questrial", sans-serif; }
  .front-brand { left: 222px; top: 848px; font-size: 19px; line-height: 22px; }
  .brand-dot { display: inline-block; width: 10px; height: 10px; border-radius: 50%;
    background: var(--red); margin-right: 6px; vertical-align: 1px; }

  .photo-agent { background: linear-gradient(180deg, #b9b2a6 0%, #a39c90 55%, #8d877c 100%);
    clip-path: polygon(34% 2%, 62% 2%, 66% 30%, 100% 52%, 100% 100%, 0 100%, 0 46%, 30% 30%); }
  .front-photo { left: 0; top: 668px; width: 186px; height: 244px; }

  /* back */
  .back-dark { left: 0; top: 0; width: 386px; height: 912px; }
  .back-pattern { left: 0; top: 0; width: 386px; height: 420px;
    background: radial-gradient(ellipse at 60% 25%, rgba(255,255,255,0.09), rgba(255,255,255,0) 70%); }

  .badge { background: var(--red); color: var(--white); font-family: "Montserrat", sans-serif;
    font-weight: 800; font-size: 22px; letter-spacing: 0.5px; border-radius: 4px;
    display: flex; align-items: center; justify-content: center; }
  .badge--sellers { left: 45px; top: 208px; width: 118px; height: 34px; }
  .badge--buyers { left: 37px; top: 446px; width: 117px; height: 34px; }
  .badge-note { color: var(--white); text-transform: uppercase; }
  .badge-note--sellers { left: 174px; top: 206px; font-size: 18px; line-height: 20px; }
  .badge-note--buyers { left: 165px; top: 446px; font-size: 15.5px; line-height: 17px; }

  .checklist { left: 33px; width: 335px; list-style: none; color: var(--white);
    font-size: 13.8px; line-height: 16.8px; }
  .checklist li { position: relative; padding-left: 15px; margin-bottom: 9.5px; }
  .checklist li svg { position: absolute; left: 0; top: 4px; }
  .checklist--sellers { top: 260px; }
  .checklist--buyers { top: 498px; }
  .example { padding-left: 15px; margin: -2px 0 10px; color: var(--white); font-size: 13.8px; line-height: 18px; }
  .example .indent { padding-left: 66px; }

  .back-brand { left: 174px; top: 636px; font-size: 28px; line-height: 30px; }
  .back-brand .second { display: block; padding-left: 48px; font-size: 25px; }
  .back-cardinal { left: 160px; top: 668px; width: 48px; height: 36px; }
  .disclaimer { left: 127px; top: 728px; color: var(--white); font-size: 11.6px; line-height: 13px; white-space: nowrap; }

  .back-photo { left: 0; top: 668px; width: 180px; height: 244px; }
  .back-name { left: 189px; top: 799px; color: var(--red); font-size: 24px; line-height: 26px; }
  .back-phone { left: 189px; top: 824px; color: var(--red); font-family: "Montserrat", sans-serif;
    font-weight: 700; font-size: 21px; line-height: 25px; }
  .back-contact { left: 189px; top: 855px; color: var(--ink); font-size: 13.8px; line-height: 17px; }
  .cert { background: #d9d9d9; border: 1px solid #9a9a9a; }
  .cert--one { left: 315px; top: 874px; width: 20px; height: 22px; }
  .cert--two { left: 338px; top: 874px; width: 22px; height: 22px; }
</style>
</head>
<body>

<svg class="crop-marks" width="960" height="1200" viewBox="0 0 960 1200" aria-hidden="true">
  <g stroke="#222" stroke-width="1">
    <line x1="80" y1="126" x2="80" y2="170"/><line x1="37" y1="170" x2="80" y2="170"/>
    <line x1="447" y1="126" x2="447" y2="170"/><line x1="447" y1="170" x2="500" y2="170"/>
    <line x1="510" y1="126" x2="510" y2="170"/>
    <line x1="877" y1="126" x2="877" y2="170"/><line x1="877" y1="170" x2="920" y2="170"/>
    <line x1="37" y1="1066" x2="80" y2="1066"/><line x1="80" y1="1066" x2="80" y2="1110"/>
    <line x1="447" y1="1066" x2="500" y2="1066"/><line x1="447" y1="1066" x2="447" y2="1110"/>
    <line x1="510" y1="1066" x2="510" y2="1110"/>
    <line x1="877" y1="1066" x2="920" y2="1066"/><line x1="877" y1="1066" x2="877" y2="1110"/>
  </g>
</svg>

<section class="hanger hanger--front">
  <div class="abs front-sky"></div>
  <div class="placeholder front-house" role="img" aria-label="Photo of a large two-storey family home with stone facade and garage under blue sky"></div>

  <svg class="abs front-dark" width="386" height="912" viewBox="0 0 386 912" aria-hidden="true">
    <defs>
      <linearGradient id="frontShade" x1="0" y1="0" x2="1" y2="1">
        <stop offset="0" stop-color="#303033"/><stop offset="1" stop-color="#222224"/>
      </linearGradient>
    </defs>
    <polygon points="0,490 194,448 386,480 386,748 0,748" fill="url(#frontShade)"/>
    <polyline points="0,486 194,444 386,476" fill="none" stroke="#e8323a" stroke-width="7"/>
  </svg>

  <div class="abs name-band"></div>
  <div class="placeholder photo-agent front-photo" role="img" aria-label="Portrait photo of the agent in a grey sweater with arms crossed"></div>

  <div class="placeholder cardinal front-cardinal" role="img" aria-label="Illustration of a red cardinal bird perched on a branch"></div>

  <p class="abs tagline tagline--one">I know the <span class="tag-mark">true value</span> of <span class="tag-mark">homes</span><br>in our neighborhood</p>
  <p class="abs tagline tagline--two">I'm not just a <span class="tag-mark">realtor</span> but I'm<br>also your <span class="tag-mark">neighbor</span></p>

  <div class="abs pitch pitch--sell">
    <h2 class="pitch-title">LOOKING TO SELL?</h2>
    <p class="pitch-text">Save thousands with my discounted<br>4.5% Full Service Listing!</p>
  </div>
  <div class="abs pitch pitch--buy">
    <h2 class="pitch-title">LOOKING TO BUY?</h2>
    <p class="pitch-text">I offer cash rebates to all my clients! $500<br>dollars credited for every $100,000 in<br>sales price.</p>
  </div>

  <p class="abs values">Honesty-Intergrity-Trust<br><span class="plain">Dependability</span><br>Neighborhood Expertise</p>

  <p class="abs front-name">MARCO DELVIN</p>
  <p class="abs front-phone">(555) 201-4478</p>
  <p class="abs front-email">RealtorMarco@mailbox.com</p>
  <p class="abs brand front-brand"><span class="brand-dot"></span>Harlow Estates</p>
</section>

<section class="hanger hanger--back">
  <svg class="abs back-dark" width="386" height="912" viewBox="0 0 386 912" aria-hidden="true">
    <defs>
      <linearGradient id="backShade" x1="0" y1="0" x2="0" y2="1">
        <stop offset="0" stop-color="#2a2a2c"/><stop offset="0.5" stop-color="#333335"/><stop offset="1" stop-color="#28282a"/>
      </linearGradient>
    </defs>
    <polygon points="0,0 386,0 386,796 147,768 0,790" fill="url(#backShade)"/>
    <rect x="0" y="0" width="386" height="5" fill="#1a1a1a"/>
    <polyline points="147,768 386,796" fill="none" stroke="#e8323a" stroke-width="5"/>
  </svg>
  <div class="abs back-pattern" role="img" aria-label="Soft geometric grey pattern background"></div>

  <div class="placeholder photo-agent back-photo" role="img" aria-label="Portrait photo of the agent in a grey sweater with arms crossed"></div>

  <div class="abs badge badge--sellers">SELLERS</div>
  <p class="abs badge-note badge-note--sellers">4.5% Full Service<br>Listing</p>

  <ul class="abs checklist checklist--sellers">
    <li><svg width="11" height="10" viewBox="0 0 11 10"><path d="M1 5 L4 8 L10 1" fill="none" stroke="#e8323a" stroke-width="1.6"/></svg>Full Time Realtor providing Expert Seller Representation</li>
    <li><svg width="11" height="10" viewBox="0 0 11 10"><path d="M1 5 L4 8 L10 1" fill="none" stroke="#e8323a" stroke-width="1.6"/></svg>Full Commission for Buying Agents</li>
    <li><svg width="11" height="10" viewBox="0 0 11 10"><path d="M1 5 L4 8 L10 1" fill="none" stroke="#e8323a" stroke-width="1.6"/></svg>Free Professional Photography</li>
    <li><svg width="11" height="10" viewBox="0 0 11 10"><path d="M1 5 L4 8 L10 1" fill="none" stroke="#e8323a" stroke-width="1.6"/></svg>Professional marketing utilizing both traditional methods (flyers, brochures, mailings, etc.) and modern platforms (search, social media, listing sites, etc.)</li>
  </ul>

  <div class="abs badge badge--buyers">BUYERS</div>
  <p class="abs badge-note badge-note--buyers">Receive $500 per<br>$100,000 of sale price</p>

  <ul class="abs checklist checklist--buyers">
    <li><svg width="11" height="10" viewBox="0 0 11 10"><path d="M1 5 L4 8 L10 1" fill="none" stroke="#e8323a" stroke-width="1.6"/></svg>I give a portion of the commission to my home buyers at settlement. Clients receive $500 per $100,000 on the sales price.</li>
    <li class="example">Example: $400,000 Home = $2,000 cash gift<br><span class="indent">$800,000 Home = $4,000 cash gift</span></li>
    <li><svg width="11" height="10" viewBox="0 0 11 10"><path d="M1 5 L4 8 L10 1" fill="none" stroke="#e8323a" stroke-width="1.6"/></svg>Full Time Realtor providing Expert Buyer Representation.</li>
  </ul>

  <p class="abs brand back-brand">Harlow<span class="second">Estates</span></p>
  <div class="placeholder cardinal back-cardinal" role="img" aria-label="Illustration of a red cardinal bird perched on a branch"></div>
  <p class="abs disclaimer">If your home is listed with another broker<br>this is not intended for solicitation.</p>

  <p class="abs back-name">MARCO DELVIN</p>
  <p class="abs back-phone">(555) 201-4478</p>
  <p class="abs back-contact">RealtorMarco@mailbox.com<br>RealtorMarco.com</p>
  <div class="abs cert cert--one" role="img" aria-label="Association membership badge"></div>
  <div class="abs cert cert--two" role="img" aria-label="Fair housing badge"></div>
</section>

</body>
</html>
```